Bramford Holloway Inc. needs an innovative idea for letterhead and visiting cards.

Bramford Holloway Inc. is a Canadian brand since 2007. It is a renown dealer of kids and office furniture locally. Moreover, exporting electric fixtures e.g. switches, LED's, down-lights etc. to Middle East and Africa. We have initiated a number of steps including re-branding, to boost our export in 2020. We have successfully designed our new logo a few months ago through 'Mockplanet' and now we are looking for an innovative idea for a letterhead.
Some key points:
• Red, black and white are the three colors used in all our packaging and furniture. (grey is optional)
• Shouldn’t be too wide.
• Use of watermark is preferable.
• You can visit our North American site at www.bramfordhollowayinc.com. Export website of the company will be launched soon. www.bramfordhollowayinc.ca
• Same letterhead will be used locally and internationally.
• Our new logo and sample packaging is attached.

```html
<!DOCTYPE html>
<html lang="en">
<head>
<meta charset="utf-8">
<title>Bramford Holloway Inc. — Business Cards</title>
<link rel="stylesheet" href="https://fonts.googleapis.com/css2?family=Open+Sans:wght@300;400;600;700&family=Libre+Baskerville&display=swap">
<style>
  :root {
    --stage: #7a7a7a;
    --card: #1d1d1f;
    --red: #a3141b;
    --white: #ffffff;
    --ink: #3a3a3c;
    --muted: #8a8a8c;
    --text-light: #f2f2f2;
    --watermark: #252527;
    --serif: "Libre Baskerville", Georgia, serif;
    --sans: "Open Sans", Arial, sans-serif;
  }
  * { box-sizing: border-box; margin: 0; padding: 0; }
  html, body { width: 1200px; height: 675px; overflow: hidden; }
  body {
    background: var(--stage);
    font-family: var(--sans);
    display: flex;
    align-items: center;
    justify-content: center;
    gap: 40px;
  }
  .card {
    position: relative;
    width: 540px;
    height: 309px;
    border-radius: 14px;
    background: var(--card);
    overflow: hidden;
    box-shadow: 0 10px 24px rgba(0,0,0,.35);
  }

  .brand { display: flex; align-items: center; gap: 16px; }
  .brand-dot {
    width: 18px; height: 18px;
    border-radius: 50%;
    background: var(--red);
    flex: none;
  }
  .brand-name {
    font-family: var(--sans);
    font-weight: 300;
    text-transform: uppercase;
    letter-spacing: 2px;
    line-height: 1.05;
    white-space: nowrap;
  }

  /* ---------- Front ---------- */
  .front .brand {
    position: absolute;
    left: 0; right: 0; top: 96px;
    justify-content: center;
  }
  .front .brand-name { color: var(--white); font-size: 34px; }
  .front .website {
    position: absolute; left: 0; right: 0; bottom: 46px;
    text-align: center; color: var(--white); font-size: 13px;
  }
  .website .domain { color: var(--red); }

  /* ---------- Back ---------- */
  .back .band {
    position: absolute; left: 0; right: 0; top: 34px; height: 74px;
    background: var(--white);
  }
  .back .brand { position: absolute; left: 24px; top: 14px; gap: 12px; }
  .back .brand-dot { width: 14px; height: 14px; }
  .back .brand-name { color: var(--ink); font-size: 22px; }
  .back .tagline {
    position: absolute; right: 22px; top: 29px;
    font-family: var(--serif); font-size: 11px;
    color: var(--ink); white-space: nowrap;
  }
  .watermark {
    position: absolute; right: 30px; top: 122px;
    width: 150px; height: 150px;
    border-radius: 50%;
    background: var(--watermark);
  }
  .contact {
    position: absolute; left: 34px; top: 138px;
    color: var(--text-light);
  }
  .contact .person {
    color: var(--red); font-weight: 700; font-size: 17px;
    text-transform: uppercase; letter-spacing: .5px;
  }
  .contact .role { font-weight: 600; font-size: 12px; margin-bottom: 10px; }
  .contact .address { font-size: 11.5px; line-height: 1.45; margin-bottom: 8px; }
  .contact ul { list-style: none; font-size: 11.5px; line-height: 1.55; }
  .contact li { display: flex; align-items: center; gap: 7px; }
  .contact svg { width: 11px; height: 11px; fill: var(--red); flex: none; }
</style>
</head>
<body>

  <section class="card front" aria-label="Business card front">
    <div class="brand">
      <span class="brand-dot"></span>
      <span class="brand-name">Bramford<br>Holloway</span>
    </div>
    <p class="website">www.<span class="domain">bramfordhollowayinc</span>.com</p>
  </section>

  <section class="card back" aria-label="Business card back">
    <div class="band">
      <div class="brand">
        <span class="brand-dot"></span>
        <span class="brand-name">Bramford<br>Holloway</span>
      </div>
      <p class="tagline">Furniture and Fixtures Since 2007</p>
    </div>

    <div class="watermark" aria-hidden="true"></div>

    <div class="contact">
      <p class="person">Dorian Pellerin</p>
      <p class="role">President</p>
      <p class="address">Unit # 22, 315 Marlow Crescent<br>Kingsford, Ontario, Canada, K9R4T2</p>
      <ul>
        <li>
          <svg viewBox="0 0 24 24" aria-hidden="true"><path d="M6.6 10.8a15.1 15.1 0 0 0 6.6 6.6l2.2-2.2a1 1 0 0 1 1-.25 11.4 11.4 0 0 0 3.6.57 1 1 0 0 1 1 1V20a1 1 0 0 1-1 1A17 17 0 0 1 3 4a1 1 0 0 1 1-1h3.5a1 1 0 0 1 1 1c0 1.25.2 2.45.57 3.57a1 1 0 0 1-.25 1z"/></svg>
          +1 888-555-0142
        </li>
        <li>
          <svg viewBox="0 0 24 24" aria-hidden="true"><path d="M2 5h20v14H2zm2 2v.5l8 5 8-5V7l-8 5z"/></svg>
          info@bramfordhollowayinc.com
        </li>
        <li>
          <svg viewBox="0 0 24 24" aria-hidden="true"><path d="M12 2a10 10 0 1 0 0 20 10 10 0 0 0 0-20zm0 2c.9 1.2 1.6 2.6 2 4h-4c.4-1.4 1.1-2.8 2-4zM4.3 14a8 8 0 0 1 0-4h3.4a16 16 0 0 0 0 4zm.8 2h3a14 14 0 0 0 1.3 3.4A8 8 0 0 1 5.1 16zm3-8h-3a8 8 0 0 1 4.3-3.4A14 14 0 0 0 8.1 8zM12 20c-.9-1.2-1.6-2.6-2-4h4c-.4 1.4-1.1 2.8-2 4zm2.3-6H9.7a14 14 0 0 1 0-4h4.6a14 14 0 0 1 0 4zm.3 5.4A14 14 0 0 0 15.9 16h3a8 8 0 0 1-4.3 3.4zM16.3 14a16 16 0 0 0 0-4h3.4a8 8 0 0 1 0 4zm-.4-6a14 14 0 0 0-1.3-3.4A8 8 0 0 1 18.9 8z"/></svg>
          www.bramfordhollowayinc.com
        </li>
      </ul>
    </div>
  </section>

</body>
</html>
```